Valto Sàrl - Business Card

VALTO Sàrl operates in the sector Services for banks and credit institutions. It is a B2B which connects companies. The main colors should be Blue and Black. The logo and look of the card should be simple, professional, conservative and reflect Connecting People.

Target Market(s)

Financial professionals and institutions

Industry/Entity Type

Finance

Contact Information for Business Card

Chemin des Prés 9
1027 Lonay

Logo Text

Connecting dots

Font styles to use
Serif
Sans Serif

Colors
0355a3
3176b5
85acd3
cfdeed

Requirements
Should not have
• Multiple colors

```html
<!DOCTYPE html>
<html lang="en">
<head>
<meta charset="utf-8">
<title>Valto Sàrl – Business Card</title>
<link rel="stylesheet" href="https://fonts.googleapis.com/css2?family=Open+Sans:wght@400;600;700&display=swap">
<style>
  :root {
    --ink: #1c1c1c;
    --paper: #ffffff;
    --blue: #4aaee3;
    --backdrop: #e9e9e9;
    --rule: #1c1c1c;
  }
  * { margin: 0; padding: 0; box-sizing: border-box; }
  html, body { width: 1200px; height: 1000px; overflow: hidden; }
  body {
    position: relative;
    background: var(--backdrop);
    font-family: "Open Sans", Arial, sans-serif;
    color: var(--ink);
  }
  .card {
    position: absolute;
    width: 665px;
    height: 397px;
    border-radius: 22px;
    overflow: hidden;
  }
  .card--front { left: 263px; top: 74px; background: var(--paper); }
  .card--back { left: 266px; top: 533px; background: var(--ink); }

  .brand {
    position: absolute;
    display: flex;
    align-items: center;
    gap: 14px;
    font-weight: 700;
    white-space: nowrap;
    letter-spacing: -0.5px;
  }
  .brand__dot { border-radius: 50%; background: var(--blue); flex: none; }
  .card--front .brand { left: 50px; top: 66px; font-size: 50px; color: var(--ink); }
  .card--front .brand__dot { width: 34px; height: 34px; }
  .card--back .brand {
    left: 0; right: 0; top: 140px; justify-content: center;
    font-size: 60px; color: var(--paper);
  }
  .card--back .brand__dot { width: 40px; height: 40px; }

  .person { position: absolute; right: 44px; top: 174px; text-align: right; }
  .person__name { font-size: 21px; font-weight: 600; line-height: 28px; }
  .person__role { font-size: 17px; color: var(--blue); line-height: 24px; }

  .divider {
    position: absolute; left: 44px; right: 44px; top: 236px;
    height: 2px; background: var(--rule);
  }

  .contact { position: absolute; left: 44px; top: 256px; list-style: none; }
  .contact li {
    display: flex; align-items: center; gap: 6px;
    font-size: 18px; line-height: 25.5px;
  }
  .contact svg { width: 17px; height: 14px; fill: var(--blue); flex: none; }

  .address {
    position: absolute; right: 44px; top: 282px;
    text-align: right; font-size: 17.5px; line-height: 24.5px; font-style: normal;
  }

  .footer-bands { position: absolute; left: 0; bottom: 0; width: 665px; height: 44px; }
  .footer-bands .band-dark { fill: var(--ink); }
  .footer-bands .band-blue { fill: var(--blue); }

  .web {
    position: absolute; font-size: 16.5px; letter-spacing: 1.3px; color: var(--paper);
  }
  .card--front .web { left: 47px; top: 360px; }
  .card--back .web { left: 0; right: 0; top: 341px; text-align: center; }
</style>
</head>
<body>
  <section class="card card--front" aria-label="Business card front">
    <div class="brand"><span class="brand__dot"></span>Valto Sàrl</div>

    <div class="person">
      <p class="person__name">Julien Marchand</p>
      <p class="person__role">CEO / Owner</p>
    </div>

    <div class="divider"></div>

    <ul class="contact">
      <li>
        <svg viewBox="0 0 17 14" aria-hidden="true"><path d="M2 4 Q8.5 -1 15 4 L13.5 6.5 L11 5.5 L11 4 Q8.5 3 6 4 L6 5.5 L3.5 6.5 Z M4.5 7.5 H12.5 L14 13 H3 Z"/></svg>
        021-555-0148
      </li>
      <li>
        <svg viewBox="0 0 17 14" aria-hidden="true"><path d="M2 4 Q8.5 -1 15 4 L13.5 6.5 L11 5.5 L11 4 Q8.5 3 6 4 L6 5.5 L3.5 6.5 Z M4.5 7.5 H12.5 L14 13 H3 Z"/></svg>
        021-555-0148 EXT 21
      </li>
      <li>
        <svg viewBox="0 0 17 14" aria-hidden="true"><path d="M1 2 H16 V12 H1 Z M2.5 3.2 L8.5 8 L14.5 3.2 V10.8 H2.5 Z" fill-rule="evenodd"/></svg>
        info@valtosarl.ch
      </li>
    </ul>

    <address class="address">
      Chemin des Prés 9<br>
      1027 Lonay, Switzerland
    </address>

    <svg class="footer-bands" viewBox="0 0 665 44" aria-hidden="true">
      <rect class="band-blue" x="360" y="20" width="305" height="24"/>
      <path class="band-dark" d="M0 0 H340 Q358 0 362 14 L372 44 H0 Z"/>
    </svg>
    <p class="web">www.valtosarl.ch</p>
  </section>

  <section class="card card--back" aria-label="Business card back">
    <div class="brand"><span class="brand__dot"></span>Valto Sàrl</div>
    <p class="web">www.valtosarl.ch</p>
  </section>
</body>
</html>
```